Security Warning Sign

We have an existing sign that needs an update. I have attached a picture of the current square sign. We need to maintain the same wording. It needs to be professional and appropriate to attach to our customers fence. Also attached is a copy of our building sign which may lend some inspiration and hopefully the ai format will assist. The final sign will be 600mm x 600mmOur website is www.halvorngate.com.au

```html
<!DOCTYPE html>
<html lang="en">
<head>
<meta charset="utf-8">
<title>Halvorngate Security – Surveillance Warning Sign</title>
<link rel="stylesheet" href="https://fonts.googleapis.com/css2?family=Roboto:wght@400;700;900&display=swap">
<style>
  :root {
    --sign-white: #ffffff;
    --sign-black: #000000;
    --sign-orange: #f47a0b;
    --brand-ink: #262626;
  }
  html, body {
    margin: 0;
    padding: 0;
    width: 1200px;
    height: 1200px;
    overflow: hidden;
    background: var(--sign-white);
  }
  .sign {
    position: relative;
    width: 1200px;
    height: 1200px;
    background: var(--sign-white);
    font-family: "Roboto", Arial, sans-serif;
  }
  .sign-graphics {
    position: absolute;
    inset: 0;
  }
  .headline {
    font-family: "Roboto", Arial, sans-serif;
    font-weight: 900;
    font-size: 262px;
    fill: var(--sign-orange);
    stroke: var(--sign-black);
    stroke-width: 7px;
    stroke-linejoin: round;
    paint-order: stroke fill;
    letter-spacing: -6px;
  }
  .notice {
    position: absolute;
    left: 0;
    top: 390px;
    width: 1200px;
    margin: 0;
    text-align: center;
    font-weight: 400;
    font-size: 96px;
    line-height: 115px;
    color: var(--sign-black);
  }
  .brand {
    position: absolute;
    left: 20px;
    top: 1045px;
    display: flex;
    align-items: center;
    gap: 26px;
  }
  .brand-mark {
    width: 150px;
    height: 150px;
    border-radius: 50%;
    background: var(--sign-orange);
  }
  .brand-name {
    margin: 0;
    font-weight: 700;
    font-size: 42px;
    line-height: 46px;
    letter-spacing: 1px;
    color: var(--brand-ink);
    text-transform: uppercase;
  }
  .phone-number {
    font-weight: 900;
    font-size: 64px;
    fill: var(--sign-white);
  }
</style>
</head>
<body>
<main class="sign">
  <svg class="sign-graphics" width="1200" height="1200" viewBox="0 0 1200 1200" aria-hidden="false">
    <defs>
      <pattern id="hazard-stripes" width="213" height="56" patternUnits="userSpaceOnUse" patternTransform="translate(75 0) skewX(-33)">
        <rect x="0" y="0" width="105" height="56" fill="var(--sign-black)"/>
      </pattern>
    </defs>

    <!-- frame -->
    <rect class="frame" x="2" y="2" width="1196" height="1196" fill="none" stroke="var(--sign-black)" stroke-width="4"/>

    <!-- hazard band -->
    <rect class="hazard-band" x="0" y="0" width="1200" height="56" fill="url(#hazard-stripes)"/>

    <!-- headline -->
    <text class="headline" x="608" y="306" text-anchor="middle">WARNING</text>

    <!-- contact band -->
    <polygon class="contact-band-accent" points="660,1102 680,1102 642,1200 622,1200" fill="var(--sign-orange)"/>
    <polygon class="contact-band" points="700,1100 1200,1100 1200,1200 662,1200" fill="var(--sign-orange)"/>

    <!-- phone icon -->
    <g class="phone-icon" transform="translate(716 1108)" fill="var(--brand-ink)">
      <path d="M14 10 C10 12 6 18 8 26 C12 40 22 52 36 58 C44 61 50 58 53 53 L46 44 C44 42 41 42 39 44 L35 47 C28 43 22 36 18 29 L22 25 C24 23 24 20 22 18 Z"/>
      <path d="M34 6 A22 22 0 0 1 56 28" fill="none" stroke="var(--brand-ink)" stroke-width="4" stroke-linecap="round"/>
      <path d="M34 16 A12 12 0 0 1 46 28" fill="none" stroke="var(--brand-ink)" stroke-width="4" stroke-linecap="round"/>
    </g>
    <text class="phone-number" x="790" y="1164">1300 418 276</text>
  </svg>

  <p class="notice">ELECTRONIC<br>SURVEILANCE<br>AND RECORDING<br>DEVICES INSTALLED<br>IN THIS AREA</p>

  <div class="brand">
    <span class="brand-mark"></span>
    <p class="brand-name">Halvorngate<br>Security<br>Services</p>
  </div>
</main>
</body>
</html>
```